Brightmoor Cleaning Services

need a brochure for my cleaning company. Contact info coming soon .

Target Market(s)

Cleaning Services

Industry/Entity Type

Cleaning Service

Requirements
Must have
• I attached logo for you to use.

Corporate address -
472 Wexley Court W Ste 118
Harlow Bay, WA 98411

Phone number - 877-555-PRISM
Nice to have
• bifold brochure. I attached some samples
Should not have
• Pictures of people. Keep it clean and professional.

```html
<!DOCTYPE html>
<html lang="en">
<head>
<meta charset="utf-8">
<title>Brightmoor Cleaning Services — Bifold Brochure</title>
<link rel="stylesheet" href="https://fonts.googleapis.com/css2?family=Montserrat:wght@400;600;700&family=Open+Sans:wght@400;600&family=Oswald:wght@500;600&display=swap">
<style>
  :root {
    --red: #e31e26;
    --red-deep: #c8141c;
    --blue: #0d4fa8;
    --blue-deep: #0a3a85;
    --gray: #b9bcc2;
    --ink: #333640;
    --paper: #ffffff;
    --canvas: #f3f5f9;
  }
  * { margin: 0; padding: 0; box-sizing: border-box; }
  html, body { width: 1200px; height: 4000px; overflow: hidden; }
  body { background: var(--canvas); font-family: "Open Sans", Arial, sans-serif; color: var(--ink); position: relative; }

  .spread { position: absolute; left: 50px; width: 1100px; height: 776px; background: var(--paper); overflow: hidden; box-shadow: 0 6px 24px rgba(0,0,0,.08); }
  .spread--outer { top: 816px; }
  .spread--inner { top: 2408px; }
  .spread svg.shapes { position: absolute; inset: 0; }
  .abs { position: absolute; }

  .heading { font-family: "Montserrat", Arial, sans-serif; font-weight: 700; font-size: 17px; letter-spacing: .3px; text-transform: uppercase; }
  .heading--blue { color: var(--blue); }
  .heading--red { color: var(--red); }
  .body-copy { font-size: 11.5px; line-height: 1.42; color: var(--ink); text-align: justify; }
  .body-copy p + p { margin-top: 16px; }

  .brand-name { display: flex; align-items: center; gap: 8px; font-family: "Montserrat", Arial, sans-serif; font-weight: 700; color: var(--blue); font-size: 19px; line-height: 1.1; }
  .brand-name .dot { width: 14px; height: 14px; border-radius: 50%; background: var(--red); flex: none; }
  .brand-name--light { color: #fff; font-size: 14px; }
  .brand-name--light .dot { background: #fff; width: 11px; height: 11px; }

  .contact { color: #fff; font-family: "Montserrat", Arial, sans-serif; font-size: 15px; line-height: 1.55; }
  .contact .phone { font-weight: 700; font-size: 20px; letter-spacing: .5px; margin-bottom: 6px; }

  .cover-title { text-align: center; }
  .cover-title .kicker { font-family: "Oswald", Arial, sans-serif; font-weight: 500; color: var(--red); font-size: 21px; letter-spacing: .2px; }
  .cover-title .title { font-family: "Oswald", Arial, sans-serif; font-weight: 600; color: var(--blue); font-size: 39px; letter-spacing: .5px; line-height: 1.15; }
  .cover-title .rule { width: 70px; height: 4px; background: var(--red); margin: 8px auto 12px; }
  .cover-title .web { font-family: "Montserrat", Arial, sans-serif; font-size: 16px; color: var(--ink); }

  .bullets { list-style: none; font-size: 11.5px; line-height: 1.42; }
  .bullets li { position: relative; padding-left: 18px; margin-bottom: 12px; }
  .bullets li::before { content: ""; position: absolute; left: 2px; top: 4px; border-left: 7px solid var(--blue); border-top: 4px solid transparent; border-bottom: 4px solid transparent; }

  .footer-web { font-family: "Montserrat", Arial, sans-serif; font-size: 13px; display: flex; align-items: center; gap: 14px; }
  .footer-web .line { width: 240px; height: 2px; background: var(--blue); }

  .panel-copy { color: #fff; font-size: 11.5px; line-height: 1.4; text-align: justify; }
</style>
</head>
<body>

<section class="spread spread--outer" aria-label="Brochure outer spread">
  <svg class="shapes" width="1100" height="776" viewBox="0 0 1100 776">
    <path d="M0,776 L0,418 C150,340 430,330 570,420 C640,470 650,610 640,776 Z" fill="var(--gray)"/>
    <path d="M0,776 L0,440 C150,362 420,352 552,440 C616,484 626,620 618,776 Z" fill="var(--red)"/>
    <path d="M410,0 L1100,0 L1100,344 C990,450 800,478 670,446 C520,408 400,250 410,0 Z" fill="var(--blue)"/>
    <g role="img" aria-label="Photo of a freshly mopped, shining commercial floor">
      <defs>
        <linearGradient id="floorPhoto" x1="0" y1="0" x2="1" y2="1">
          <stop offset="0" stop-color="#8fa6c2"/>
          <stop offset=".55" stop-color="#dfe6ee"/>
          <stop offset="1" stop-color="#c6d0dc"/>
        </linearGradient>
      </defs>
      <path d="M440,0 L1100,0 L1100,318 C990,416 810,442 680,414 C540,382 432,240 440,0 Z" fill="url(#floorPhoto)"/>
    </g>
    <g role="img" aria-label="Photo of a bucket of cleaning supplies and gloves">
      <rect x="262" y="60" width="176" height="210" rx="18" fill="#f2c33b" opacity=".85"/>
    </g>
  </svg>

  <div class="abs" style="left:42px; top:66px; width:208px;">
    <h2 class="heading heading--blue" style="margin-bottom:14px;">Lorem Ipsum</h2>
    <div class="body-copy" style="font-size:10.5px;">
      <p>Lorem Ipsum is simply dummy text of the printing and typesetting industry. Lorem Ipsum has been the industry's standard dummy text ever since the 1500s, when an unknown printer took a galley of type and scrambled it to make a type specimen book. It has survived not only five centuries, but also the leap into electronic typesetting, remaining essentially unchanged.</p>
      <p>Lorem Ipsum is simply dummy text of the printing and typesetting industry. Lorem Ipsum has been the industry's standard dummy text ever since the 1500s, when an unknown printer took a galley of type and scrambled it to make a type specimen book.</p>
    </div>
  </div>

  <div class="abs contact" style="left:236px; top:558px;">
    <div class="phone">877-555-PRISM</div>
    <div>info@yourwebsite.com</div>
    <div>www.yourwebsite.com</div>
    <div>472 Wexley Court W Ste 118</div>
    <div>Harlow Bay, WA 98411</div>
  </div>

  <div class="abs brand-name brand-name--light" style="left:52px; top:640px; width:150px;">
    <span class="dot"></span><span>Brightmoor Cleaning Services</span>
  </div>

  <div class="abs brand-name" style="left:770px; top:500px; width:220px;">
    <span class="dot"></span><span>Brightmoor Cleaning Services</span>
  </div>

  <div class="abs cover-title" style="left:640px; top:580px; width:420px;">
    <div class="kicker">LOREM IPSUM IS SIMPLY DUMMY</div>
    <div class="title">TEXT OF THE PRINTING</div>
    <div class="rule"></div>
    <div class="web">www.yourwebsite.com</div>
  </div>
</section>

<section class="spread spread--inner" aria-label="Brochure inner spread">
  <svg class="shapes" width="1100" height="776" viewBox="0 0 1100 776">
    <path d="M0,0 L540,0 C560,150 520,320 380,360 C250,396 120,360 0,320 Z" fill="var(--red)"/>
    <path d="M0,0 L520,0 C540,146 500,300 372,338 C250,372 120,338 0,300 Z" fill="var(--gray)"/>
    <g role="img" aria-label="Photo of a sofa and carpet being vacuumed">
      <defs>
        <linearGradient id="carpetPhoto" x1="0" y1="0" x2="1" y2="1">
          <stop offset="0" stop-color="#e6e2dc"/>
          <stop offset="1" stop-color="#9aa0a8"/>
        </linearGradient>
      </defs>
      <path d="M0,0 L506,0 C524,140 486,290 364,324 C246,356 120,324 0,288 Z" fill="url(#carpetPhoto)"/>
    </g>

    <path d="M550,776 L550,590 C680,520 900,500 1100,488 L1100,776 Z" fill="var(--red)"/>
    <path d="M550,776 L550,608 C680,540 900,522 1100,512 L1100,776 Z" fill="var(--blue)"/>
    <g role="img" aria-label="Photo of a blue spray bottle and cleaning cloth">
      <defs>
        <linearGradient id="sprayPhoto" x1="0" y1="0" x2="1" y2="0">
          <stop offset="0" stop-color="#1e5fb8"/>
          <stop offset="1" stop-color="#0d4fa8"/>
        </linearGradient>
      </defs>
      <path d="M550,776 L550,622 C620,582 700,566 760,562 C800,630 800,730 770,776 Z" fill="url(#sprayPhoto)" opacity=".9"/>
    </g>
  </svg>

  <div class="abs" style="left:48px; top:396px; width:440px;">
    <h2 class="heading heading--red" style="margin-bottom:14px;">Lorem Ipsum Dolor</h2>
    <div class="body-copy">
      <p>Ut diam tortor, maximus sed lorem quis, vulputate scelerisque sapien. Ut mollis sapien et arcu elementum, sit amet cursus nisl semper. Suspendisse velit felis, laoreet eget laoreet vel, iaculis vel massa. Integer quis elit eleifend, pharetra sem ut, sodales orci. Duis dapibus sit amet est et rutrum. Maecenas sit amet neque vel neque blandit tempus sed sit amet ante. Pellentesque finibus egestas porta. Vivamus cursus dui magna, tempus dictum orci sodales sit amet. Vivamus vel arcu quis mi pulvinar blandit. Donec et nibh facilisis, venenatis nunc et.</p>
      <p>Ut diam tortor, maximus sed lorem quis, vulputate scelerisque sapien. Ut mollis sapien et arcu elementum, sit amet cursus nisl semper. Suspendisse velit felis, laoreet eget laoreet vel, iaculis vel massa. Integer quis elit eleifend, pharetra sem ut, sodales orci. Duis dapibus sit amet est et rutrum. Maecenas sit amet neque vel neque blandit tempus sed sit amet ante. Pellentesque finibus egestas porta. Vivamus cursus dui magna, tempus dictum orci sodales sit amet. Vivamus vel arcu quis mi pulvinar blandit. Donec et nibh facilisis, venenatis nunc et.</p>
    </div>
  </div>
  <div class="abs footer-web" style="left:48px; top:728px;">
    <span>www.yourwebsite.com</span><span class="line"></span>
  </div>

  <div class="abs" style="left:588px; top:58px; width:470px;">
    <h2 class="heading heading--blue" style="margin-bottom:12px;">Ut Mollis Sapien Et</h2>
    <div class="body-copy">
      <p>Integer tempor mollis vestibulum. Etiam velit turpis, lobortis ac euismod et, porta in tortor. Nulla suscipit, lectus sed tincidunt elementum, justo massa malesuada justo, in iaculis nisi arcu ut magna. Morbi tristique convallis augue sit amet mattis. Pellentesque eu leo quis leo rhoncus pulvinar. Duis lacinia dolor sit amet dapibus lacinia. Donec sodales laoreet ornare.</p>
    </div>
  </div>

  <div class="abs" style="left:588px; top:232px; width:230px;">
    <h2 class="heading heading--red" style="margin-bottom:12px;">Sem Egestas Dolor</h2>
    <div class="body-copy">
      <p>Integer tempor mollis vestibulum. Etiam velit turpis, lobortis ac euismod et, porta in tortor. Nulla suscipit, lectus sed tincidunt elementum, justo massa malesuada justo, in iaculis nisi arcu ut magna. Morbi tristique convallis augue sit amet mattis. Pellentesque eu leo quis leo rhoncus pulvinar. Duis lacinia dolor sit amet dapibus lacinia. Donec sodales laoreet ornare.</p>
    </div>
  </div>

  <div class="abs" style="left:844px; top:232px; width:216px;">
    <h2 class="heading heading--red" style="margin-bottom:12px;">Ultricies Risus</h2>
    <ul class="bullets">
      <li>Lorem ipsum dolor sit amet, consectetur adipiscing elit.</li>
      <li>Curabitur cursus, neque quis faucibus convallis, libero urna ultrices diam</li>
      <li>Curabitur cursus, neque quis faucibus convallis, libero urna ultrices diam</li>
    </ul>
  </div>

  <div class="abs" style="left:830px; top:548px; width:236px;">
    <h2 class="heading heading--red" style="margin-bottom:12px; font-size:15px;">Ut Mollis Sapien Et</h2>
    <div class="panel-copy">Integer tempor mollis vestibulum. Etiam velit turpis, lobortis ac euismod et, porta in tortor. Nulla suscipit, lectus sed tincidunt elementum, justo massa malesuada justo, in iaculis nisi arcu ut magna. Morbi tristique convallis augue sit amet mattis. Pellentesque eu leo quis leo rhoncus pulvinar. Duis lacinia dolor sit amet dapibus lacinia. Donec sodales laoreet ornare.</div>
  </div>
</section>

</body>
</html>
```